NOLV.
ALWAYS BESIDE YOU
NOLV. -
Creative Brief
Use specific fonts
any thing which suits with the LOGO provided
Professional
RAHUL MEHTA
MR.
D-47, NORTH PARK-III, GURGAON 122019, HARYANA, INDIA
rahul@nolv.co
www.nolv.co
use logo at centre

```html
<!DOCTYPE html>
<html lang="en">
<head>
<meta charset="utf-8">
<title>NOLV. Business Cards</title>
<link rel="stylesheet" href="https://fonts.googleapis.com/css2?family=Open+Sans:wght@400;600;700;800&display=swap">
<style>
  :root {
    --bg: #e9e6e2;
    --card: #ffffff;
    --red: #e3222b;
    --red-dark: #b3141b;
    --charcoal: #3a3a3c;
    --text: #333333;
    --rule: #c8c8c8;
  }
  * { box-sizing: border-box; margin: 0; padding: 0; }
  html, body { width: 1200px; height: 852px; overflow: hidden; }
  body {
    background: var(--bg);
    font-family: "Open Sans", Arial, sans-serif;
    color: var(--text);
    position: relative;
  }
  .card {
    position: absolute;
    width: 560px;
    height: 320px;
    background: var(--card);
    border-radius: 22px;
    overflow: hidden;
    box-shadow: 0 6px 18px rgba(0,0,0,0.18);
  }
  .card--front { left: 70px; top: 80px; }
  .card--back { left: 570px; top: 452px; }

  .swoosh { position: absolute; left: 0; bottom: 0; width: 560px; height: 110px; }

  .brand { display: flex; align-items: center; gap: 10px; }
  .brand__mark { border-radius: 50%; background: var(--red); flex: none; }
  .brand__name { font-weight: 800; color: var(--red); line-height: 1; letter-spacing: 1px; }
  .brand__tagline { font-weight: 700; color: var(--charcoal); font-size: 14px; letter-spacing: 0.5px; margin-top: 6px; }

  .divider { position: absolute; width: 1px; background: var(--rule); }

  .person__name { color: var(--red); font-weight: 700; font-size: 17px; letter-spacing: 0.3px; }
  .person__address { font-size: 12.5px; line-height: 1.45; color: var(--text); margin-top: 6px; }

  .contacts { list-style: none; }
  .contacts li { display: flex; align-items: center; gap: 8px; font-size: 12.5px; line-height: 1; height: 19px; }
  .contacts svg { width: 13px; height: 13px; flex: none; }

  /* front card layout */
  .card--front .brand-block { position: absolute; left: 30px; top: 88px; width: 220px; }
  .card--front .brand__mark { width: 40px; height: 40px; }
  .card--front .brand__name { font-size: 46px; }
  .card--front .divider { left: 262px; top: 34px; height: 190px; }
  .card--front .person { position: absolute; left: 284px; top: 36px; width: 260px; }
  .card--front .contacts { position: absolute; left: 284px; top: 114px; }

  /* back card layout */
  .card--back .brand-block { position: absolute; left: 150px; top: 40px; }
  .card--back .brand__mark { width: 46px; height: 46px; }
  .card--back .brand__name { font-size: 56px; }
  .card--back .brand-block .brand__tagline { text-align: right; }
  .card--back .person { position: absolute; left: 34px; top: 152px; width: 220px; text-align: center; }
  .card--back .divider { left: 276px; top: 146px; height: 100px; }
  .card--back .contacts { position: absolute; left: 296px; top: 150px; }
</style>
</head>
<body>

<section class="card card--front" aria-label="Business card, layout one">
  <div class="brand-block">
    <div class="brand">
      <span class="brand__mark"></span>
      <span class="brand__name">NOLV.</span>
    </div>
    <div class="brand__tagline">ALWAYS BESIDE YOU</div>
  </div>
  <div class="divider"></div>
  <div class="person">
    <div class="person__name">RAHUL MEHTA</div>
    <div class="person__address">D-47, North Park-III, Gurgaon 122019,<br>Haryana, India</div>
  </div>
  <ul class="contacts">
    <li><svg viewBox="0 0 16 16"><path fill="var(--red)" d="M3 1h3l1.5 4-2 1.3a9 9 0 0 0 4.2 4.2L11 8.5l4 1.5v3c0 1-1 2-2 2A12 12 0 0 1 1 3c0-1 1-2 2-2z"/></svg>+91-124-5550182</li>
    <li><svg viewBox="0 0 16 16"><rect x="4" y="1" width="8" height="14" rx="1.5" fill="var(--red)"/><rect x="5.5" y="3" width="5" height="8" fill="#fff"/></svg>+91-9876500213</li>
    <li><svg viewBox="0 0 16 16"><rect x="1" y="6" width="14" height="8" rx="1" fill="var(--red)"/><rect x="4" y="1" width="8" height="6" fill="var(--charcoal)"/></svg>+91-124-5550947</li>
    <li><svg viewBox="0 0 16 16"><circle cx="8" cy="8" r="7" fill="var(--red)"/><path d="M4 5.5h8v5H4z" fill="#fff"/><path d="M4 5.5l4 3 4-3" fill="none" stroke="var(--red)" stroke-width="1"/></svg>rahul@nolv.co</li>
    <li><svg viewBox="0 0 16 16"><circle cx="8" cy="8" r="7" fill="var(--red)"/><circle cx="8" cy="8" r="4" fill="none" stroke="#fff" stroke-width="1.3"/><path d="M4 8h8M8 4v8" stroke="#fff" stroke-width="1"/></svg>www.nolv.co</li>
  </ul>
  <svg class="swoosh" viewBox="0 0 560 110" preserveAspectRatio="none" aria-hidden="true">
    <defs>
      <linearGradient id="redBandA" x1="0" y1="0" x2="0" y2="1">
        <stop offset="0" stop-color="#f0464d"/>
        <stop offset="1" stop-color="#b3141b"/>
      </linearGradient>
    </defs>
    <path d="M0 40 C150 80 330 95 560 66 L560 110 L0 110 Z" fill="url(#redBandA)"/>
    <path d="M0 28 C150 68 330 84 560 58 L560 70 C330 96 150 84 0 48 Z" fill="var(--charcoal)"/>
    <path d="M0 36 C150 74 330 90 560 62 L560 66 C330 94 150 80 0 42 Z" fill="#ffffff"/>
  </svg>
</section>

<section class="card card--back" aria-label="Business card, layout two">
  <div class="brand-block">
    <div class="brand">
      <span class="brand__mark"></span>
      <span class="brand__name">NOLV.</span>
    </div>
    <div class="brand__tagline">ALWAYS BESIDE YOU</div>
  </div>
  <div class="person">
    <div class="person__name">RAHUL MEHTA</div>
    <div class="person__address">D-47, North Park-III,<br>Gurgaon 122019,<br>Haryana, India</div>
  </div>
  <div class="divider"></div>
  <ul class="contacts">
    <li><svg viewBox="0 0 16 16"><path fill="var(--red)" d="M3 1h3l1.5 4-2 1.3a9 9 0 0 0 4.2 4.2L11 8.5l4 1.5v3c0 1-1 2-2 2A12 12 0 0 1 1 3c0-1 1-2 2-2z"/></svg>+91-124-5550182</li>
    <li><svg viewBox="0 0 16 16"><rect x="4" y="1" width="8" height="14" rx="1.5" fill="var(--red)"/><rect x="5.5" y="3" width="5" height="8" fill="#fff"/></svg>+91-9876500213</li>
    <li><svg viewBox="0 0 16 16"><rect x="1" y="6" width="14" height="8" rx="1" fill="var(--red)"/><rect x="4" y="1" width="8" height="6" fill="var(--charcoal)"/></svg>+91-124-5550947</li>
    <li><svg viewBox="0 0 16 16"><circle cx="8" cy="8" r="7" fill="var(--red)"/><path d="M4 5.5h8v5H4z" fill="#fff"/><path d="M4 5.5l4 3 4-3" fill="none" stroke="var(--red)" stroke-width="1"/></svg>rahul@nolv.co</li>
    <li><svg viewBox="0 0 16 16"><circle cx="8" cy="8" r="7" fill="var(--red)"/><circle cx="8" cy="8" r="4" fill="none" stroke="#fff" stroke-width="1.3"/><path d="M4 8h8M8 4v8" stroke="#fff" stroke-width="1"/></svg>www.nolv.co</li>
  </ul>
  <svg class="swoosh" viewBox="0 0 560 110" preserveAspectRatio="none" aria-hidden="true">
    <defs>
      <linearGradient id="redBandB" x1="0" y1="0" x2="0" y2="1">
        <stop offset="0" stop-color="#f0464d"/>
        <stop offset="1" stop-color="#b3141b"/>
      </linearGradient>
    </defs>
    <path d="M0 62 C150 92 330 100 560 78 L560 110 L0 110 Z" fill="url(#redBandB)"/>
    <path d="M0 52 C150 82 330 90 560 68 L560 80 C330 102 150 96 0 70 Z" fill="var(--charcoal)"/>
    <path d="M0 60 C150 88 330 96 560 74 L560 78 C330 100 150 92 0 64 Z" fill="#ffffff"/>
  </svg>
</section>

</body>
</html>
```